Ledgerwise Reach - B2B Demand Generation Website Project

We need a fully functional website for www.ledgerwisereach.example. We are a B2B Demand Generation company, based in London, working with companies such as QRT, VKD, Norvex, Brindlow, Tarvo generating them sales leads for their sales teams. We run this through digital marketing newsletter promotions and have a network of websites. Content syndication, data, demand generation, online marketing. Our logo has just been redone (attached) and we have a holding page already which i would like to use the style / colours. Our logo is bright and vibrant but i dont want the site to be a rainbow. We are expensive, classy, professorial, B2B, intelligent.

Home
About Us
Our Services
Prospora & QA Technology
Intent Data
Testimonials
Contact Us
Updates

Target Market(s)

B2B Marketers (QRT, Velquarion, Tarvo, VKD, Opal Reach, Driftmoor, Harlow Quantis, Technology Companies, Data Companies, Marketing Teams, Tumbleden.

Industry/Entity Type

Marketing

Coding

Coded - Design and coding required

Number of Pages Required

5+ page

Font styles to use
Sans Serif

Requirements
Must have
• Home
About Us
Our Services
Prospora & QA Technology
Intent Data
Testimonials
Contact Us

Simple Pages.

Look classy, intelligent, data experts. I like the video homepages were the image moves at the top. Very soft animation.
Nice to have
• Websites i like:

https://www.vkd.example/
https://www.brevantor.example/
https://www.plumfieldsites.example.co.uk/

Ledgerwise Reach - The Demand Generation Company
Should not have
• Glimpsevault crap images

```html
<!DOCTYPE html>
<html lang="en">
<head>
<meta charset="utf-8">
<title>Ledgerwise Reach - The Demand Generation Company</title>
<link rel="stylesheet" href="https://fonts.googleapis.com/css2?family=Poppins:wght@400;500&family=Montserrat:wght@600;700&family=Roboto:wght@400&display=swap">
<style>
:root{
  --brand-red:#c9252c;
  --brand-blue:#2a8db5;
  --nav-blue:#2a7fa6;
  --ink:#333333;
  --band:#f6f4f4;
  --footer:#0a81ad;
  --footer-bar:#0774a0;
  --white:#ffffff;
}
*{margin:0;padding:0;box-sizing:border-box}
html,body{width:1200px;height:2542px;overflow:hidden;background:var(--white)}
body{position:relative;font-family:'Poppins',sans-serif;color:var(--ink)}
.abs{position:absolute}

.site-header{left:0;top:0;width:1200px;height:108px;background:var(--white)}
.brand{left:47px;top:30px;display:flex;align-items:center;gap:8px}
.brand-dot{width:22px;height:22px;border-radius:50%;background:var(--brand-red)}
.brand-name{font-size:20px;font-weight:500;color:var(--brand-red);line-height:1}
.brand-tag{left:77px;top:58px;font-size:8px;color:var(--brand-red)}
.main-nav a{position:absolute;top:68px;font-size:14px;color:var(--nav-blue);text-decoration:none;white-space:nowrap}

.hero{left:0;top:108px;width:1200px;height:520px;
  background:
    radial-gradient(circle at 288px 345px,rgba(8,32,70,.85) 0,rgba(10,50,100,.55) 70px,transparent 170px),
    radial-gradient(ellipse at 760px 330px,rgba(120,200,240,.35) 0,transparent 320px),
    radial-gradient(ellipse at 150px 120px,rgba(110,190,235,.45) 0,transparent 300px),
    linear-gradient(110deg,#1f7cc0 0%,#1567aa 35%,#0d4f8e 60%,#041a32 100%);
  border-bottom:3px solid #5cb6e0}
.hero-title{left:659px;top:364px;font-family:'Roboto',sans-serif;color:var(--white)}
.hero-title .name{font-size:28px;line-height:32px}
.hero-title .sub{font-size:17px;line-height:22px}

.intro{left:139px;top:732px;width:940px;font-size:22px;line-height:33px;color:var(--ink)}
.intro .inline-brand{color:var(--brand-red);font-size:26px}
.intro .inline-brand.small{font-size:22px}

.section-title{left:0;top:1046px;width:1200px;text-align:center;font-family:'Montserrat',sans-serif;font-weight:700;font-size:32px;color:var(--brand-blue)}
.client-band{left:0;top:1123px;width:1200px;height:144px;background:var(--band)}
.client{position:absolute;top:56px;transform:translateX(-50%);font-size:22px;font-weight:500;white-space:nowrap}
.client.q{color:#1f58b5}.client.t{color:#c9252c}.client.v{color:#222}
.client.o{color:#e2463a}.client.d{color:#0a72b8}.client.c{color:#1a9ee0}

.reach{left:0;top:1351px;width:1200px;height:600px;
  background:linear-gradient(100deg,#3f6f9a 0%,#6f95b7 35%,#5a7fa4 60%,#27436a 100%)}
.reach-heading{left:59px;top:1582px;width:360px;font-family:'Montserrat',sans-serif;font-weight:700;font-size:36px;line-height:42px;color:var(--white)}

.stat{top:1877px;width:308px;height:211px;background:var(--white);border:1px solid #cfcfcf;text-align:center}
.stat .num{margin-top:44px;font-family:'Montserrat',sans-serif;font-weight:600;font-size:48px;color:var(--brand-blue);line-height:60px}
.stat .label{margin-top:20px;font-size:17px;color:var(--ink)}

.site-footer{left:0;top:2206px;width:1200px;height:264px;background:var(--footer);color:var(--white)}
.footer-bar{left:0;top:2470px;width:1200px;height:72px;background:var(--footer-bar);color:var(--white);font-size:14px}
.f-head{font-size:16px}
.f-text{font-size:13px;line-height:21px}
.social{display:flex;gap:8px}
.social span{font-size:13px;display:flex;align-items:center;gap:4px}
.social i{width:10px;height:10px;border-radius:50%;background:var(--white);display:inline-block}
.subscribe{left:868px;top:2335px;width:210px;height:30px;border:1px solid var(--white);display:flex}
.subscribe .field{flex:1;background:var(--white);color:#2a7fa6;font-size:11px;padding:8px 0 0 18px}
.subscribe .send{width:32px;display:flex;align-items:center;justify-content:center}
.footer-bar a{position:absolute;top:34px;color:var(--white);text-decoration:none}
</style>
</head>
<body>

<header class="abs site-header">
  <div class="abs brand"><span class="brand-dot"></span><span class="brand-name">Ledgerwise Reach</span></div>
  <div class="abs brand-tag">The Demand Generation Company</div>
  <nav class="main-nav">
    <a style="left:363px">Home</a>
    <a style="left:436px">About Us</a>
    <a style="left:531px">Our Services</a>
    <a style="left:653px">Prospora &amp; QA Tecnology</a>
    <a style="left:853px">Intent Data</a>
    <a style="left:963px">Testimonials</a>
    <a style="left:1080px">Contact</a>
  </nav>
</header>

<section class="abs hero" role="img" aria-label="Abstract blue dotted spiral background with soft motion"></section>
<div class="abs hero-title">
  <div class="name">Ledgerwise Reach</div>
  <div class="sub">The Demand Generation Company</div>
</div>

<p class="abs intro"><span class="inline-brand">Ledgerwise Reach</span> offers multi-channel demand generation services to publishers and technology vendors through our network of lead generation websites and native speaking telemarketing agents. Whether looking for MQL, ABM or BANT campaigns, <span class="inline-brand small">Ledgerwise Reach</span> can assist you in delivering your demand generation strategy and generate pipeline for your sales teams and/or channel partners.</p>

<h2 class="abs section-title">Who We Work With</h2>
<div class="abs client-band">
  <span class="client q" style="left:190px">QRT</span>
  <span class="client t" style="left:356px">Tarvo</span>
  <span class="client v" style="left:523px">VKD</span>
  <span class="client o" style="left:726px">Orrelan</span>
  <span class="client d" style="left:904px">Dunmarr</span>
  <span class="client c" style="left:1042px">Cloudvane</span>
</div>

<section class="abs reach" role="img" aria-label="Business person in an office overlooking a city, with a world map network overlay"></section>
<h2 class="abs reach-heading">High quality sales leads from any country in the world</h2>

<div class="abs stat" style="left:110px"><div class="num">70000+</div><div class="label">Downloads Per Month</div></div>
<div class="abs stat" style="left:447px"><div class="num">25000+</div><div class="label">Leads Delivered per Month</div></div>
<div class="abs stat" style="left:783px"><div class="num">50+</div><div class="label">Countries We Can Reach</div></div>

<footer class="abs site-footer">
  <div class="abs f-head" style="left:122px;top:85px">Ledgerwise Reach</div>
  <div class="abs social" style="left:70px;top:132px">
    <span><i></i>Kestrel</span><span><i></i>Orbit</span><span><i></i>Lumen</span><span><i></i>Weave</span>
  </div>
  <div class="abs f-head" style="left:357px;top:85px">Address</div>
  <div class="abs f-text" style="left:357px;top:118px">Fenwick Yard Road, 214, London,<br>England SE9 4QX, GB</div>
  <div class="abs f-text" style="left:357px;top:188px">27 Millbrook Lane, 84, London,<br>England TW9 2LK, GB</div>
  <div class="abs f-head" style="left:659px;top:85px">Phone</div>
  <div class="abs" style="left:659px;top:118px;font-size:16px">0208 5550147</div>
  <div class="abs f-head" style="left:868px;top:85px">Subscribe Using Email</div>
</footer>
<div class="abs subscribe">
  <div class="field">Type Your Email</div>
  <div class="send"><svg width="16" height="16" viewBox="0 0 16 16" fill="none" stroke="#fff" stroke-width="1"><path d="M1 7 L15 1 L10 15 L7 9 Z M7 9 L15 1"/></svg></div>
</div>

<div class="abs footer-bar">
  <a style="left:88px">contact</a>
  <a style="left:177px">Terms Of Use</a>
  <a style="left:303px">Privacy</a>
  <a style="left:390px">Our Policy</a>
  <a style="left:868px">Copyright ©2020 All rights reserved</a>
</div>

</body>
</html>
```